Prairie Civic Builders Summit (PCBS) needs a flyer and logo design

We need a save the date flyer that can be easily edited to be a header only with event title, date and location.
We also are looking for a conference logo that will go well with our company logo.
Updates
Most of you are submitting an agenda design. Not a graphic flyer design. This isn't what I'm needing. I need something that can easily be a save the date with a header and is graphically appealing. Additionally, I've only gotten 2 logo designs.
Target Market(s)
Architects, engineers, public owners, contractors, attorneys
Industry/Entity Type
Construction
Logo Text
Prairie Civic Builder's Summit
Requirements
Must have
- Flyer should Have:
- Title: "The Lantern across Quiet Meadows - Project Delivery to Operations”
- Date: August 8-9, 2019
- Location: Fort Worth, TX
- One-page only
- Conference Logo should be relatable to our company logo: Prairie Civic Builders Summit.
Nice to have
- Topics:
- Alternative Constrcting: JOC & Design-Build
- Dealing with Contracting in a Tight TX Industry
- Tools & Technologies Project Delivery and Operations: Design and Construction
- Tools & Technologies: Coordinating Operations
Should not have
- Detailed agenda

```html
<!DOCTYPE html>
<html lang="en">
<head>
<meta charset="utf-8">
<title>Prairie Civic Builders Summit – Save the Date</title>
<link rel="stylesheet" href="https://fonts.googleapis.com/css2?family=PT+Sans:wght@400;700&family=PT+Serif:wght@700&display=swap">
<style>
  :root {
    --navy: #15132f;
    --band-blue: #1f4596;
    --mark-blue: #2a4fa3;
    --text-light: #e9e9ee;
    --logo-grey: #d5d6da;
    --accent-green: #8db33e;
  }
  * { margin: 0; padding: 0; box-sizing: border-box; }
  html, body {
    width: 848px;
    height: 1200px;
    overflow: hidden;
    background: var(--navy);
  }
  .flyer {
    position: relative;
    width: 848px;
    height: 1200px;
    background: var(--navy);
    font-family: "PT Sans", Arial, sans-serif;
    color: var(--text-light);
  }
  .brand {
    position: absolute;
    left: 36px;
    top: 40px;
    width: 314px;
  }
  .brand-square {
    display: block;
    width: 96px;
    height: 96px;
    margin-left: 104px;
    background: var(--mark-blue);
  }
  .brand-name {
    display: block;
    margin-top: 26px;
    font-size: 76px;
    font-weight: 700;
    letter-spacing: 6px;
    line-height: 1;
    color: var(--logo-grey);
  }
  .brand-full {
    display: block;
    margin-top: 8px;
    font-family: "PT Serif", Georgia, serif;
    font-weight: 700;
    font-size: 18.5px;
    color: var(--accent-green);
    white-space: nowrap;
  }
  .event-title {
    position: absolute;
    left: 40px;
    right: 30px;
    top: 385px;
    text-align: center;
    font-weight: 400;
    font-size: 62px;
    line-height: 86px;
    color: var(--text-light);
  }
  .info-band {
    position: absolute;
    left: 0;
    width: 489px;
    height: 91px;
  }
  .info-band svg {
    position: absolute;
    inset: 0;
  }
  .info-band p {
    position: relative;
    padding-left: 26px;
    line-height: 91px;
    font-size: 34px;
    color: #ffffff;
  }
  .band-date { top: 849px; }
  .band-location { top: 969px; }
  .footer-bar {
    position: absolute;
    left: 0;
    top: 1133px;
    width: 848px;
    height: 33px;
    background: var(--accent-green);
  }
</style>
</head>
<body>
<main class="flyer">
  <header class="brand">
    <span class="brand-square"></span>
    <span class="brand-name">PCBS</span>
    <span class="brand-full">Prairie Civic Builders Summit</span>
  </header>

  <h1 class="event-title">The Lantern across Quiet Meadows - Project Delivery to Operations</h1>

  <div class="info-band band-date">
    <svg width="489" height="91" viewBox="0 0 489 91" aria-hidden="true">
      <polygon points="0,0 489,0 418,91 0,91" fill="var(--band-blue)"/>
    </svg>
    <p>Date : August 8-9, 2019</p>
  </div>

  <div class="info-band band-location">
    <svg width="489" height="91" viewBox="0 0 489 91" aria-hidden="true">
      <polygon points="0,0 489,0 418,91 0,91" fill="var(--band-blue)"/>
    </svg>
    <p>Location : Fort Worth, TX</p>
  </div>

  <div class="footer-bar"></div>
</main>
</body>
</html>
```